New design for www.TrimTable.com

On TrimTable you can find & book your hairdresser. TrimTable is the biggest platform in the Netherlands.

- The design should be a responcive design
- Should be able to go global, should fit in perfectly between all the big booking platforms like roomquay, zipvan etc,
- Should have te result of more bookings. :)
- We are ‘only’ asking a beautiful design, not a technical solution.
- We need a homepage (https://trimtable.com/), search resultpage ((https://trimtable.com/kapper/amsterdam/#), salonpage (https://trimtable.com/kapper/vorden/sol-mira-hair/), about us page (https://trimtable.com/aboutus/), for the hairdresser info page (https://trimtable.com/kapper/), login/register page (https://trimtable.com/account/signin/).

- On the page of the hairdresser there is a dynamic part. The part where you create your appointment. Please take a look at this part too after you choose your treatment (behandeling), employee (medewerker), Date (datum) and time (tijd). The part that you see after this, is the part where you fill in your data as a consumer.

I've added more logo's but mostly we use the green color.

A few of our competitors: www.glowpick.com, www.kestoly.com

Target Market(s)

All consumers

Industry/Entity Type

Hair And Beauty

Number of Pages Required

5+ page

Font styles to use
Sans Serif

Colors
abd036
c3c3c3
757575

Requirements
Must have
• Responsive
• We did an A/B test with the homepage. It turns out that option B works better then option A (take a look at the uploaded pictures). So what we need on the homepage: The USP's with the green checkboxes, The search button needs to by dynamic (changes for example from light green to dark green so you can see you can click it) The call to action sentence Zoek & Vind je kapsalon, the searchfield and searchbutton should be seperated.
Nice to have
• The style that we like is the flat design style. The website should be simple, clean and it should feel a bit like a luxury thing. Because an appointment with the hairdresser can be a real treat and luxury moment for yourself.
• The luxury feeling and flat design that is in the www.zipvan.com website is really nice for example. But then it has to be a bit more light and not so black and dark.

```html
<!DOCTYPE html>
<html lang="en">
<head>
<meta charset="utf-8">
<title>TrimTable – Zoek &amp; Vind je kapsalon</title>
<link rel="stylesheet" href="https://fonts.googleapis.com/css2?family=Roboto:wght@300;400;500;700&display=swap">
<style>
:root{
  --green:#abd036;
  --green-dark:#8fb321;
  --grey-light:#c3c3c3;
  --grey:#757575;
  --ink:#333333;
  --paper:#ffffff;
  --mist:#f2f2f2;
  --night:#3b3b3b;
  --night-deep:#2a2a2a;
}
*{box-sizing:border-box;margin:0;padding:0}
html,body{width:1200px;height:2736px;overflow:hidden}
body{font-family:"Roboto",Arial,sans-serif;color:var(--ink);background:var(--paper)}
section,header,footer{position:relative;width:1200px;overflow:hidden}

/* hero */
.hero{height:780px;color:var(--paper)}
.hero-photo{position:absolute;inset:0;background:linear-gradient(160deg,#6c6a66 0%,#3f3d3a 45%,#8a8580 75%,#4a4845 100%)}
.hero-shade{position:absolute;inset:0;background:rgba(20,20,20,.45)}
.hero-chevron{position:absolute;left:0;bottom:0}
.top-links{position:absolute;top:14px;right:40px;font-size:12px;letter-spacing:1px;display:flex;gap:14px}
.top-links span+span{border-left:1px solid rgba(255,255,255,.6);padding-left:14px}
.brand{position:absolute;top:150px;left:0;width:100%;display:flex;justify-content:center;align-items:center;gap:14px}
.brand-dot{width:46px;height:46px;border-radius:50%;background:var(--paper)}
.brand-name{font-size:46px;font-weight:400;color:var(--paper)}
.hero-title{position:absolute;top:270px;width:100%;text-align:center;font-size:50px;font-weight:500}
.search{position:absolute;top:366px;left:340px;display:flex;gap:10px}
.search-field{width:418px;height:50px;background:var(--paper);border-radius:2px;color:#9a9a9a;font-size:15px;padding:16px 18px}
.search-button{width:120px;height:50px;background:var(--green);color:var(--paper);font-size:16px;font-weight:500;letter-spacing:1px;text-align:center;line-height:50px;border-radius:2px;box-shadow:inset 0 -4px 0 var(--green-dark)}
.search-hint{position:absolute;top:426px;left:346px;font-size:12px;color:rgba(255,255,255,.8)}
.usps{position:absolute;top:500px;width:100%;display:flex;justify-content:center;gap:60px;font-size:15px}
.usp{display:flex;align-items:center;gap:10px}

/* stats */
.stats{height:180px;display:flex;justify-content:center;gap:70px;padding-top:30px}
.stat{width:150px;text-align:center}
.stat svg{display:block;margin:0 auto 8px}
.stat-value{font-size:34px;font-weight:300;color:var(--ink)}
.stat-label{font-size:10px;font-weight:500;letter-spacing:.5px;color:var(--grey);text-transform:uppercase;margin-top:4px}

/* steps */
.steps{height:160px;display:flex;justify-content:center;padding-top:20px}
.step{width:355px;height:100px;border:1px solid var(--grey-light);border-left:none;text-align:center;padding-top:20px}
.step:first-child{border-left:1px solid var(--grey-light)}
.step-title{font-size:22px;font-weight:400}
.step-text{font-size:12px;color:var(--grey);margin-top:8px;line-height:1.4;padding:0 50px}

/* reviews */
.reviews{height:280px}
.reviews-photo{position:absolute;inset:0;background:linear-gradient(90deg,#c98d6a 0%,#e7c3a6 22%,#b9b2a8 45%,#8e8780 100%)}
.review-card{position:absolute;top:70px;left:640px;width:480px;height:150px;background:rgba(40,40,40,.82);color:var(--paper);padding:20px 30px}
.review-title{font-size:26px;font-weight:300}
.review-quote{font-size:15px;line-height:1.45;margin-top:8px;font-style:italic}
.review-author{font-size:12px;color:var(--grey-light);margin-top:8px}

/* app */
.app{height:390px;background:var(--paper)}
.app-band{position:absolute;left:0;top:0}
.app-phone{position:absolute;top:30px;left:170px;width:310px;height:340px;border-radius:30px;background:linear-gradient(150deg,#fdfdfd 0%,#e6e6e6 55%,#cfd8bb 100%)}
.app-copy{position:absolute;top:90px;left:620px;width:540px}
.app-kicker{font-size:18px;color:var(--grey)}
.app-title{font-size:36px;font-weight:300;line-height:1.15;margin-top:8px}
.app-title b{font-weight:700;color:var(--ink)}
.app-text{font-size:16px;color:var(--grey);margin-top:12px;line-height:1.4;width:480px}
.app-button{display:inline-flex;align-items:center;gap:10px;margin-top:20px;background:var(--grey);color:var(--paper);padding:12px 26px;border-radius:4px;font-size:16px}

/* cards */
.cards{height:320px;display:flex;justify-content:center;gap:20px;padding-top:30px}
.card{width:265px;text-align:center}
.card-photo{height:170px}
.card-title{font-size:20px;font-weight:500;margin-top:16px}
.card-text{font-size:12px;color:var(--grey);line-height:1.4;margin:6px 30px 0}

/* newsletter */
.newsletter{height:100px;display:flex;align-items:center;padding:0 115px;border-top:1px solid #e5e5e5}
.newsletter-title{font-size:30px;font-weight:400}
.newsletter-text{font-size:11px;color:var(--grey);width:330px;line-height:1.35;margin-top:2px}
.newsletter-form{margin-left:auto;display:flex}
.newsletter-field{width:220px;height:40px;border:1px solid var(--grey-light);font-size:12px;color:var(--grey);padding:13px 12px}
.newsletter-button{width:100px;height:40px;background:var(--night);color:var(--paper);font-size:14px;text-align:center;line-height:40px}

/* help */
.help{height:190px;background:var(--night);color:var(--paper)}
.help-title{text-align:center;font-size:36px;font-weight:300;padding-top:28px}
.help-actions{display:flex;justify-content:center;gap:70px;margin-top:36px;font-size:13px}
.help-action{display:flex;align-items:center;gap:10px}
.help-ring{width:38px;height:38px;border:1px solid var(--grey-light);border-radius:50%;display:flex;align-items:center;justify-content:center}
.social{position:absolute;right:60px;top:122px;display:flex;gap:8px}
.social span{width:30px;height:30px;background:var(--grey);border-radius:3px}

/* places */
.places{height:240px;background:var(--night-deep);color:var(--paper);padding:30px 60px 0}
.places-title{font-size:22px;font-weight:400}
.places-text{font-size:12px;color:var(--grey-light);margin-top:8px;line-height:1.45;width:1040px}
.places-list{display:grid;grid-template-columns:repeat(5,200px);row-gap:10px;margin-top:20px;list-style:none;font-size:12px;color:var(--grey-light)}
.places-list li{display:flex;align-items:center;gap:8px}
.places-list li::before{content:"";width:10px;height:10px;border:1px solid var(--grey-light);border-radius:2px}
.places-list li.places-gap::before{display:none}

/* bottom */
.legal{height:96px;background:var(--night-deep);color:var(--grey-light);padding:10px 60px;font-size:11px;line-height:1.7;border-top:1px solid #444}
.legal a{color:var(--paper);text-decoration:underline}
</style>
</head>
<body>

<header class="hero">
  <div class="hero-photo" role="img" aria-label="Photograph of a barber salon interior with chairs and mirrors"></div>
  <div class="hero-shade"></div>
  <nav class="top-links"><span>LOGIN</span><span>REGISTER</span></nav>
  <div class="brand"><span class="brand-dot"></span><span class="brand-name">TrimTable</span></div>
  <h1 class="hero-title">Zoek &amp; Vind je kapsalon</h1>
  <div class="search">
    <div class="search-field">Stad en plaats of postcode</div>
    <div class="search-button">SEARCH</div>
  </div>
  <div class="search-hint">or search within radius</div>
  <div class="usps">
    <div class="usp"><svg width="22" height="22" viewBox="0 0 22 22"><path d="M3 11l5 5 11-11" fill="none" stroke="#abd036" stroke-width="3"/></svg>TrimTable largest booking site NL</div>
    <div class="usp"><svg width="22" height="22" viewBox="0 0 22 22"><path d="M3 11l5 5 11-11" fill="none" stroke="#abd036" stroke-width="3"/></svg>Appointments with 100% certainty</div>
    <div class="usp"><svg width="22" height="22" viewBox="0 0 22 22"><path d="M3 11l5 5 11-11" fill="none" stroke="#abd036" stroke-width="3"/></svg>More than 20,000 TrimTable reviews</div>
  </div>
  <svg class="hero-chevron" width="1200" height="120" viewBox="0 0 1200 120"><polygon points="0,30 600,120 1200,30 1200,120 0,120" fill="#ffffff"/></svg>
</header>

<section class="stats">
  <div class="stat">
    <svg width="52" height="52" viewBox="0 0 52 52" fill="none" stroke="#757575" stroke-width="2"><rect x="14" y="6" width="24" height="22" rx="3"/><rect x="10" y="28" width="32" height="8"/><path d="M16 36v10M36 36v10M12 46h28"/></svg>
    <div class="stat-value">542</div><div class="stat-label">Salons</div>
  </div>
  <div class="stat">
    <svg width="52" height="52" viewBox="0 0 52 52" fill="none" stroke="#757575" stroke-width="2"><circle cx="26" cy="26" r="20"/><path d="M16 26l7 7 13-14"/></svg>
    <div class="stat-value">16.375</div><div class="stat-label">Treatments for booking</div>
  </div>
  <div class="stat">
    <svg width="52" height="52" viewBox="0 0 52 52" fill="none" stroke="#757575" stroke-width="2"><path d="M6 24l10-10 10 6 10-6 10 10-14 14-6-6-6 6z"/><path d="M20 30l6 6M24 26l6 6"/></svg>
    <div class="stat-value">571.377</div><div class="stat-label">Appointments</div>
  </div>
  <div class="stat">
    <svg width="52" height="52" viewBox="0 0 52 52" fill="none" stroke="#757575" stroke-width="2"><circle cx="26" cy="16" r="9"/><path d="M8 46c0-12 8-18 18-18s18 6 18 18"/></svg>
    <div class="stat-value">7.171</div><div class="stat-label">Hairdressers booking</div>
  </div>
  <div class="stat">
    <svg width="52" height="52" viewBox="0 0 52 52" fill="#757575"><polygon points="26,4 30,15 41,15 32,22 35,33 26,26 17,33 20,22 11,15 22,15"/><polygon points="12,30 14,36 20,36 15,40 17,46 12,42 7,46 9,40 4,36 10,36"/><polygon points="40,30 42,36 48,36 43,40 45,46 40,42 35,46 37,40 32,36 38,36"/></svg>
    <div class="stat-value">26.603</div><div class="stat-label">Reliable reviews</div>
  </div>
</section>

<section class="steps">
  <div class="step"><div class="step-title">1. Discover</div><p class="step-text">Search for beauty &amp; wellness salons in your area</p></div>
  <div class="step"><div class="step-title">2. Book</div><p class="step-text">Choose your service and book an appointment directly from the salon calendar</p></div>
  <div class="step"><div class="step-title">3. Enjoy</div><p class="step-text">Sit back and enjoy your unique beauty &amp; wellness experience</p></div>
</section>

<section class="reviews">
  <div class="reviews-photo" role="img" aria-label="Photograph of a smiling customer in a hair salon"></div>
  <div class="review-card">
    <h2 class="review-title">Helpful Reviews</h2>
    <p class="review-quote">"Thanks to the many reviews on the website I can find my new hairdresser via TrimTable!"</p>
    <p class="review-author">Lieke, Amsterdam</p>
  </div>
</section>

<section class="app">
  <svg class="app-band" width="1200" height="390" viewBox="0 0 1200 390"><polygon points="0,0 1200,0 1200,60 0,330" fill="#f2f2f2"/></svg>
  <div class="app-phone" role="img" aria-label="Illustration of a smartphone showing the TrimTable app"></div>
  <div class="app-copy">
    <p class="app-kicker">Anywhere, Anytime</p>
    <h2 class="app-title">All the <b>hairdressers</b><br>of Netherlands in your pocket?</h2>
    <p class="app-text">Download the Kavrodo APP and always find a place to make a good hairday off.</p>
    <span class="app-button"><svg width="18" height="18" viewBox="0 0 18 18"><path d="M9 2v10M4 8l5 5 5-5M3 16h12" fill="none" stroke="#fff" stroke-width="2"/></svg>Download Kavrodo APP</span>
  </div>
</section>

<section class="cards">
  <article class="card"><div class="card-photo" role="img" aria-label="Photograph of a hair collection" style="background:linear-gradient(135deg,#5a4a40,#c9b39c)"></div><h3 class="card-title">Collection</h3><p class="card-text">Lorem Ipsum is simply dummy text of the printing and typesetting industry.</p></article>
  <article class="card"><div class="card-photo" role="img" aria-label="Photograph of hairstyle inspiration" style="background:linear-gradient(135deg,#8a7a6e,#e2d6c8)"></div><h3 class="card-title">Inspiration</h3><p class="card-text">Lorem Ipsum is simply dummy text of the printing and typesetting industry.</p></article>
  <article class="card"><div class="card-photo" role="img" aria-label="Photograph of a stylist giving advice" style="background:linear-gradient(135deg,#6b5448,#d8b8a0)"></div><h3 class="card-title">Style Advice</h3><p class="card-text">Lorem Ipsum is simply dummy text of the printing and typesetting industry.</p></article>
  <article class="card"><div class="card-photo" role="img" aria-label="Photograph of a salon event" style="background:linear-gradient(135deg,#4e4744,#b7aaa2)"></div><h3 class="card-title">News &amp; Events</h3><p class="card-text">Lorem Ipsum is simply dummy text of the printing and typesetting industry.</p></article>
</section>

<section class="newsletter">
  <div>
    <h2 class="newsletter-title">Just Style Enewsletter</h2>
    <p class="newsletter-text">Sign up for our newsletter to receive the latest trends, promotions and style advice from the TrimTable team.</p>
  </div>
  <div class="newsletter-form"><div class="newsletter-field">Your e-mail address</div><div class="newsletter-button">Subscribe</div></div>
</section>

<section class="help">
  <h2 class="help-title">We're here to help</h2>
  <div class="help-actions">
    <div class="help-action"><span class="help-ring"><svg width="18" height="18" viewBox="0 0 18 18"><path d="M4 2l3 4-2 2c1 2 3 4 5 5l2-2 4 3-2 3C8 16 2 10 2 4z" fill="#c3c3c3"/></svg></span>Talk to a person</div>
    <div class="help-action"><span class="help-ring"><svg width="18" height="18" viewBox="0 0 18 18" fill="none" stroke="#c3c3c3" stroke-width="1.5"><rect x="2" y="4" width="14" height="12"/><path d="M2 8h14M6 2v4M12 2v4"/></svg></span>Book an appointment</div>
    <div class="help-action"><span class="help-ring"><svg width="18" height="18" viewBox="0 0 18 18" fill="none" stroke="#c3c3c3" stroke-width="1.5"><path d="M2 4h14v9H7l-4 3v-3H2z"/></svg></span>Request a call</div>
  </div>
  <div class="social"><span></span><span></span><span></span><span></span><span></span></div>
</section>

<section class="places">
  <h2 class="places-title">Make an appointment at the hairdresser in one of these places.</h2>
  <p class="places-text">Choose a hairdresser and book your appointment directly. Below you find a small selection of cities in the Netherlands. Looking for a salon in another place? Use the search field and discover all hairdressers near you. What are you waiting for? Make an appointment today.</p>
  <ul class="places-list">
    <li>Barber Amsterdam</li><li>Barber Rotterdam</li><li>Barber Hague</li><li>Barber Utrecht</li><li>Barber Eindhoven</li>
    <li>Barber Tilburg</li><li>Barber Groningen</li><li>Barber Arnhem</li><li>Barber Breda</li><li class="places-gap"></li>
    <li>Barber Nijmegen</li><li>Barber Haarlem</li>
  </ul>
</section>

<footer class="legal">
  <p><a>About Us</a> | <a>Read our blog</a></p>
  <p>Copyright © 2015 TrimTable • All rights reserved</p>
  <p>Legal | Disclaimer | Terms and Conditions</p>
</footer>

</body>
</html>
```